Simple templates for management consulting firm

Vireo Associates is a management consulting firm based in the DC area. We have all the basic templates but would like to tweak them so they look consistent.

Check us out at www.vireoassociates-example.com

For this project we would like to get
a tweaked powerpoint template (header should be up)
a letter template for letters
a fax template

Current templates and our logo are attached.
Updates

We just increased the budget of this project.

We got questions about the project. Here are our thoughts on this one:

Please include the logo into the fax template. If you find improvements in the layout then feel free to make those. Let's not overthink this too much. Keep it simple :)

We like The powerpoint concept as is. The slide titles are for some reasons on the bottom. It seems to irritate some folks. If you can switch the slide titles to the top, keep the look and feel of the slides and work in the logo then that would be fantastic.

The letter head should include the following

Vireo Associates, LLC Box 5827, Millbrook, VA 20147 Phone 703 518-9461, Fax 703 286 7135, www.vireoassociates-example.com and the logo.

Again, let's keep it simple.

Thank you for considering this project.

We just realize that we are not necessarily inisting to use the red in the slides.
Any approach that would work with the logo will be considered.

Thanks for your creativity.

Target Market(s)

tech companies, Pinnacle 400, venture capitalists

Industry/Entity Type

Management Consulting

Requirements
Must have
• Keep it simple please

```html
<!DOCTYPE html>
<html lang="en">
<head>
<meta charset="utf-8">
<title>Vireo Associates – Stationery Templates</title>
<link rel="stylesheet" href="https://fonts.googleapis.com/css2?family=Libre+Baskerville&family=Montserrat:wght@400;500;600&family=Open+Sans:wght@400;600&display=swap">
<style>
  :root{
    --page:#ffffff;
    --ink:#1e1a1a;
    --muted:#6d6d6d;
    --label:#a9a9a9;
    --wine:#5a0d14;
    --red:#8e0f1c;
    --blush:#f3dede;
    --gold:#b58b3a;
    --line:#c9c9c9;
  }
  *{margin:0;padding:0;box-sizing:border-box}
  html,body{width:1200px;height:960px;overflow:hidden;background:var(--page)}
  body{position:relative;font-family:"Open Sans",Arial,sans-serif;color:var(--ink)}

  .sheet{position:absolute;background:#fff;box-shadow:0 2px 10px rgba(0,0,0,.28);overflow:hidden}
  .label{position:absolute;font-family:"Open Sans",Arial,sans-serif;font-size:14px;color:var(--label)}

  .brand{position:absolute;display:flex;align-items:center;gap:6px;font-family:"Libre Baskerville",Georgia,serif;color:var(--gold);white-space:nowrap}
  .brand-dot{border-radius:50%;background:var(--gold);flex:none}

  .band{position:absolute;left:0;right:0;bottom:0;display:flex;align-items:center;justify-content:center;color:#fff;font-family:"Montserrat",Arial,sans-serif}
  .band-red{background:linear-gradient(90deg,var(--blush) 0%,var(--blush) 14%,var(--red) 28%,var(--wine) 50%,var(--red) 72%,var(--blush) 86%,var(--blush) 100%)}
  .band-grey{background:linear-gradient(90deg,#e9e9e9 0%,#9a9a9a 30%,#2f2f2f 50%,#9a9a9a 70%,#e9e9e9 100%)}

  /* Letter */
  .letter{left:17px;top:19px;width:551px;height:713px}
  .letter .brand{left:25px;top:30px;font-size:21px}
  .letter .brand-dot{width:32px;height:32px}
  .letter-body{position:absolute;left:26px;top:138px;width:510px;font-family:"Libre Baskerville",Georgia,serif;font-size:10.3px;line-height:21.6px;color:var(--ink)}
  .letter-body p{margin-bottom:21.6px}
  .letter-body .sign{padding-left:237px;margin-top:21.6px}
  .letter-address{position:absolute;left:0;right:0;top:672px;text-align:center;font-family:"Montserrat",Arial,sans-serif;font-size:9.6px;color:var(--muted)}
  .letter .band{height:22px;font-size:10px}

  /* Fax */
  .fax{left:839px;top:22px;width:338px;height:440px;font-family:"Montserrat",Arial,sans-serif;color:var(--wine)}
  .fax .brand{left:14px;top:12px;font-size:11px}
  .fax .brand-dot{width:13px;height:13px}
  .fax-title{position:absolute;right:14px;top:26px;font-size:36px;font-weight:600;color:#111}
  .fax-sender{position:absolute;left:14px;top:34px;font-size:6px;line-height:8px;color:#333}
  .fax-date{position:absolute;left:14px;top:70px;font-size:6px;color:#333}
  .rule{position:absolute;left:0;right:0;height:1px;background:linear-gradient(90deg,transparent,#555 20%,#555 80%,transparent)}
  .fax-grid{position:absolute;font-size:6px;line-height:7.4px}
  .fax-grid b{font-weight:600}
  .fax-checks{position:absolute;left:8px;top:368px;list-style:none;font-size:6px;color:#333}
  .fax-checks li{display:flex;align-items:center;gap:6px;height:14px}
  .fax-checks li::before{content:"";width:6px;height:6px;border:1px solid #999}
  .fax .band{height:13px;font-size:6.5px}

  /* Slides */
  .slide{background:radial-gradient(ellipse at 50% 40%,#ffffff 0%,#f4f4f4 40%,#d6d6d6 100%);font-family:"Montserrat",Arial,sans-serif}
  .slide-title{left:590px;top:497px;width:590px;height:455px}
  .slide-title .brand{left:22px;top:22px;font-size:16px}
  .slide-title .brand-dot{width:20px;height:20px}
  .slide-company{position:absolute;left:22px;top:253px;font-size:17.5px;font-weight:500;color:var(--wine)}
  .slide-name{position:absolute;left:22px;top:306px;font-size:21px;font-weight:600;color:var(--wine)}
  .slide-role{position:absolute;left:22px;top:332px;font-size:14px;color:var(--wine)}
  .slide-title .band{height:22px;font-size:9px}

  .slide-agenda{left:306px;top:750px;width:262px;height:202px}
  .slide-agenda .brand{left:10px;top:8px;font-size:9px}
  .slide-agenda .brand-dot{width:10px;height:10px}
  .agenda-heading{position:absolute;left:10px;top:26px;font-size:15px;font-weight:500;color:var(--wine)}
  .agenda-list{position:absolute;left:10px;top:58px;list-style:none;font-size:7.8px;line-height:13px;color:var(--wine)}
  .agenda-list li::before{content:"•";color:var(--red);margin-right:3px}
  .agenda-list .sub{padding-left:10px;font-size:6.6px}
  .slide-agenda .band{height:8px;font-size:4.5px}
</style>
</head>
<body>

<span class="label" style="left:580px;top:21px">letter template</span>
<span class="label" style="left:740px;top:21px">fax template</span>
<span class="label" style="left:593px;top:469px">powerpoint template</span>
<span class="label" style="left:151px;top:935px">powerpoint template</span>

<!-- Letterhead -->
<section class="sheet letter">
  <div class="brand"><span class="brand-dot"></span>VIREO ASSOCIATES</div>
  <div class="letter-body">
    <p>Jumpstarting your business means to take what you have to the next level.<br>
    Quickly. Very often there is an insight of “What brought us here, doesn’t get us where we want to be.” This is where Vireo Associates comes into play. We give our clients an helping hand when it comes to increasing your sales performance along with the required operational changes. We deliver results fast, because all of our clients have a business to run. They cannot take an off-year.</p>
    <p>They need to deliver results to stay competitive in their own market while getting to the next level. We understand. Our approach is hand-on and practical based on a deep understanding of methodologies that work and the experience of putting these into practice.</p>
    <p>Jumpstarting your business means to take what you have to the next level.<br>
    Quickly. Very often there is an insight of “What brought us here, doesn’t get us where we want to be.” This is where Vireo Associates comes into play. We give our clients an helping hand when it comes to increasing your sales performance along with the required operational changes. We deliver results fast, because all of our clients have a business to run. They cannot take an off-year.</p>
    <p class="sign">the experience of putting these into practice.</p>
  </div>
  <div class="letter-address">Vireo Associates, LLC Box 5827, Millbrook, VA 20147 / Phone: 703 518-9461 /Fax: 703 286 7135</div>
  <div class="band band-red">www.vireoassociates-example.com</div>
</section>

<!-- Fax -->
<section class="sheet fax">
  <div class="brand"><span class="brand-dot"></span>VIREO ASSOCIATES</div>
  <div class="fax-sender">VIREO ASSOCIATES, LLC<br>www.vireoassociates-example.com<br>P 703 512 6604<br>F 703 286 7135</div>
  <div class="fax-title">Fax</div>
  <div class="fax-date">1/24/2012</div>
  <div class="rule" style="top:80px"></div>
  <div class="fax-grid" style="left:14px;top:84px">TO:«GreetingLine»<br>[TYPE THE RECIPIENT COMPANY NAME]<br>FAX:«Business Fax»<br>PHONE:«Business Phone»<br><br>CC:[Type text]<br>RE:[Type text]</div>
  <div class="fax-grid" style="left:176px;top:84px">FROM:<b>Lukas Brenner</b><br>PAGES:[Type the number of pages]<br>FAX:[Type the sender fax number]<br>PHONE:[Type the sender phone number]</div>
  <div class="rule" style="top:136px"></div>
  <div class="fax-grid" style="left:14px;top:140px">COMMENTS:<br>[Type comments]</div>
  <div class="rule" style="top:364px"></div>
  <ul class="fax-checks">
    <li>Urgent</li><li>Please review</li><li>Please comment</li><li>For your records</li>
  </ul>
  <div class="band band-grey">www.vireoassociates-example.com</div>
</section>

<!-- Title slide -->
<section class="sheet slide slide-title">
  <div class="brand"><span class="brand-dot"></span>VIREO ASSOCIATES</div>
  <div class="slide-company">VIREO ASSOCIATES</div>
  <div class="slide-name">Owen Hartley</div>
  <div class="slide-role">Managing Partner</div>
  <div class="band band-red">Copyright © 2012 | Vireo Associates</div>
</section>

<!-- Agenda slide -->
<section class="sheet slide slide-agenda">
  <div class="brand"><span class="brand-dot"></span>VIREO ASSOCIATES</div>
  <h2 class="agenda-heading">Agenda</h2>
  <ul class="agenda-list">
    <li>Jumpstart Your Business</li>
    <li class="sub">Mastering the Sale</li>
    <li class="sub">Getting Projects Done</li>
    <li class="sub">Turnaround</li>
    <li>Vireo Associates’ Engagement Model</li>
    <li>About Lukas Brenner</li>
  </ul>
  <div class="band band-red">Copyright © 2012 | Vireo Associates</div>
</section>

</body>
</html>
```